Ebook-Cover für Bodybuilding- bzw. Fitnessbuch
Zielgruppe
Es handelt sich um einen Ratgeber für Bodybuilder, die Schwierigkeiten haben, Muskelmasse aufzubauen.
Aufgabenstellung
Ich stelle mir einen durchtrainierten Männeroberkörper vor, evtl. beim Training. Das Bild soll nicht allzu reißerisch sein, damit es nicht unseriös wirkt. Es soll aber auch nicht zu bieder sein. Es sollte auch in schwarz/weiß ansehnlich sein. Der abgebildete Bodybuilder soll nicht allzu extrem sein, er sollte eine durchtrainierte aber noch natürliche Statur haben, wie ein kräftiger Kampfsportler.
Das Buch soll bei Kaufhaven verkauft werden. Dementsprechend sollte es als Miniaturansicht in der Cover-Vorschau erkennbar und Titel und Untertitel lesbar sein.
Titel und Untertitel sollen auf das Cover. Der Titel heißt "Das Pollwerk-Prinzip" und der Untertitel "Kraftsport für breite Schultern".
Mein Autoren-Name "Lutger Mahrenz" soll ebenfalls auf das Cover.
Update 09.02. nach Design #6:
Vielen Dank an alle Designer für die ersten Designs! Die Designs gehen grundsätzlich in die richtige Richtung. Allerdings sind mir die abgebildeten Sportler doch etwas zu schlank, es darf doch ein wenig mehr Muskulatur vorhanden sein!

```html
<!DOCTYPE html>
<html lang="de">
<head>
<meta charset="utf-8">
<title>Das Pollwerk-Prinzip – Lutger Mahrenz</title>
<link rel="stylesheet" href="https://fonts.googleapis.com/css2?family=Bebas+Neue&family=Montserrat:wght@800&display=swap">
<style>
  :root {
    --orange: #f45c04;
    --white: #ffffff;
    --photo-dark: #1c1209;
    --photo-mid: #4a2f16;
    --photo-warm: #6b4522;
  }
  html, body {
    margin: 0;
    padding: 0;
    width: 900px;
    height: 1200px;
    overflow: hidden;
    background: var(--photo-dark);
  }
  .cover {
    position: relative;
    width: 900px;
    height: 1200px;
    overflow: hidden;
  }
  .cover-photo {
    position: absolute;
    inset: 0;
    background:
      radial-gradient(ellipse at 35% 25%, var(--photo-warm) 0%, transparent 55%),
      radial-gradient(ellipse at 70% 80%, var(--photo-mid) 0%, transparent 60%),
      linear-gradient(160deg, var(--photo-mid) 0%, var(--photo-dark) 70%);
  }
  .cover-art {
    position: absolute;
    inset: 0;
  }
  .badge-shape { fill: var(--orange); }
  .author-label,
  .author-name,
  .feature-list {
    font-family: 'Bebas Neue', 'Oswald', sans-serif;
    fill: var(--white);
  }
  .author-label { font-size: 84px; }
  .author-name { font-size: 78px; }
  .feature-list { font-size: 31px; }
  .title-line,
  .title-accent,
  .subtitle {
    font-family: 'Montserrat', 'Arial Black', sans-serif;
    font-weight: 800;
  }
  .title-line { fill: var(--white); font-size: 112px; }
  .title-accent { fill: var(--orange); font-size: 150px; }
  .subtitle { fill: var(--white); font-size: 46px; }
</style>
</head>
<body>
<main class="cover">
  <div class="cover-photo" role="img" aria-label="Foto: Kurzhanteln mit schwarzen Gewichtsscheiben und Trainingsgurten im Studio, warm beleuchtet"></div>

  <svg class="cover-art" width="900" height="1200" viewBox="0 0 900 1200" xmlns="http://www.w3.org/2000/svg">
    <!-- Autorenfeld -->
    <path class="badge-shape" d="M 600 44 H 865 V 261 C 830 275 800 284 770 284 C 660 284 574 205 574 112 C 574 82 584 60 600 44 Z"/>
    <text class="author-label" x="838" y="126" text-anchor="end">AUTOR</text>
    <text class="author-name" x="838" y="224" text-anchor="end" textLength="330" lengthAdjust="spacingAndGlyphs">LUTGER MAHRENZ</text>

    <!-- Titel -->
    <text class="title-line" x="453" y="411" text-anchor="middle">DAS</text>
    <text class="title-accent" x="40" y="636" textLength="831" lengthAdjust="spacingAndGlyphs">PRINZIP</text>
    <text class="title-line" x="40" y="543" textLength="831" lengthAdjust="spacingAndGlyphs">POLLWERK-</text>
    <text class="subtitle" x="35" y="712" textLength="833" lengthAdjust="spacingAndGlyphs">KRAFTSPORT FÜR BREITE SCHULTERN</text>

    <!-- Inhaltsfeld -->
    <path class="badge-shape" d="M 32 1000 C 32 966 60 944 120 944 C 225 944 292 1030 296 1160 H 32 Z"/>
    <text class="feature-list">
      <tspan x="54" y="1014">MAXIMALE TRAININGSDAUER</tspan>
      <tspan x="54" y="1051">TRAININGSINTENSITÄT</tspan>
      <tspan x="54" y="1088">INTENSITÄTSWECHSEL</tspan>
      <tspan x="54" y="1127">VIELFALT IN DER ÜBUNGSAUSWAHL</tspan>
    </text>
  </svg>
</main>
</body>
</html>
```